Restaurant needs a vertical banner for fried catfish

Our restaurant is looking for an eye-catching 78.75in. x 36in. vertical physical banner ad for our fried catfish. Photos for the fried catfish will be provided as a reference but we will also accept anything similar to the photo. We will be using the following as our receptacle: https://www.plankoria.example/banner-stand/retractable-banner-stands/
The design must incorporate the following flavor texts:
Fried Catfish
Always Fresh!
Made from Scratch
Hand-cut Fillets
The Best Catfish in Texas
Served with fries, hush puppies, and a 32oz fountain drink
Also available by the pound!
The final design should be creative, professional, and eye-catching for customers.
Updates
Colors
Designer to choose colors to be used in the design.
Requirements
Must have
- We are open to any and all design elements, albeit the 'flavor texts' should not overpower, but complement the fried catfish photo. 'Fried Catfish' can be used in lieu of a main title/logo.
Nice to have
- Transparent or textured backgrounds that can encompass any or all part of the banner such as a cutting board, shadows, abstract, etc to show depth are a plus.
- Use of vectors or objects such as ribbons or shapes to encapsulate the 'flavor texts' are also encouraged.

```html
<!DOCTYPE html>
<html lang="en">
<head>
<meta charset="utf-8">
<title>Fried Catfish – Vertical Banner</title>
<link rel="stylesheet" href="https://fonts.googleapis.com/css2?family=Open+Sans:wght@400;700&family=Lobster&display=swap">
<style>
  :root {
    --backdrop: #c9c9c9;
    --paper: #ecebe4;
    --paper-fleck: #dcdad0;
    --green: #3f9e70;
    --teal: #7fbcb6;
    --ink: #2a2a2a;
    --white: #ffffff;
    --photo-top: #d8c8c0;
    --photo-mid: #d9b94e;
    --photo-low: #8f7158;
  }
  * { box-sizing: border-box; margin: 0; padding: 0; }
  html, body {
    width: 1200px; height: 1000px; overflow: hidden;
    background: var(--backdrop);
  }
  .canvas {
    position: relative; width: 1200px; height: 1000px;
    display: flex; align-items: center; justify-content: center;
  }
  .banner {
    position: relative; width: 410px; height: 940px;
    background:
      radial-gradient(circle at 20% 30%, var(--paper-fleck) 0 1px, transparent 2px) 0 0 / 23px 19px,
      radial-gradient(circle at 70% 60%, var(--paper-fleck) 0 1px, transparent 2px) 0 0 / 31px 27px,
      var(--paper);
    display: flex; flex-direction: column;
    font-family: "Open Sans", sans-serif;
    color: var(--ink);
  }
  .banner-header {
    height: 130px; text-align: center; padding-top: 20px;
  }
  .banner-title {
    font-weight: 700; font-size: 53px; line-height: 1;
    color: var(--green); letter-spacing: 0.5px;
  }
  .banner-tagline {
    font-size: 30px; line-height: 1; margin-top: 12px;
  }
  .product-photo {
    height: 532px;
    background: linear-gradient(180deg, var(--photo-top) 0%, var(--photo-mid) 50%, var(--photo-low) 100%);
  }
  .banner-details {
    flex: 1; display: flex; flex-direction: column; align-items: center;
    padding-top: 26px;
  }
  .feature-ribbon { width: 350px; height: 110px; display: block; }
  .ribbon-text {
    font-family: "Open Sans", sans-serif; font-size: 15.5px; fill: var(--white);
  }
  .badge-text {
    font-family: "Open Sans", sans-serif; font-size: 11px; fill: var(--white);
  }
  .badge-script {
    font-family: "Lobster", cursive; font-size: 24px; fill: var(--white);
  }
  .serving-note {
    margin-top: 18px; text-align: center; font-size: 16px; line-height: 1.35;
  }
  .banner-footer {
    height: 58px; background: var(--green); color: var(--white);
    display: flex; align-items: center; justify-content: center;
    font-size: 25px;
  }
</style>
</head>
<body>
<main class="canvas">
  <article class="banner">
    <header class="banner-header">
      <h1 class="banner-title">FRIED CATFISH</h1>
      <p class="banner-tagline">Always Fresh!</p>
    </header>

    <div class="product-photo" role="img" aria-label="Photo of golden cornmeal-crusted fried catfish fillets on a white plate with fresh herbs, on a wooden table"></div>

    <section class="banner-details">
      <svg class="feature-ribbon" viewBox="0 0 350 110" aria-label="Made from scratch, hand-cut fillets. The best catfish in Texas">
        <polygon points="0,14 350,14 350,94 0,94 28,54" fill="var(--teal)"/>
        <polygon points="22,20 344,20 344,88 22,88 44,54" fill="var(--green)"/>
        <text class="ribbon-text" x="44" y="47">MADE FROM SCRATCH</text>
        <text class="ribbon-text" x="44" y="77">HAND-CUT FILLETS</text>
        <circle cx="276" cy="56" r="52" fill="var(--teal)"/>
        <circle cx="276" cy="56" r="43" fill="none" stroke="var(--white)" stroke-width="2.5"/>
        <text class="badge-text" x="276" y="40" text-anchor="middle">The Best</text>
        <text class="badge-text" x="276" y="55" text-anchor="middle">Catfish in</text>
        <text class="badge-script" x="276" y="81" text-anchor="middle">Texas</text>
      </svg>
      <p class="serving-note">Served with fries, hush puppies,<br>and a 32oz fountain drink.</p>
    </section>

    <footer class="banner-footer">Also available by the pound!</footer>
  </article>
</main>
</body>
</html>
```